Need a small Brochure Designing for a High Tech LED Spotlight

This is an expensive product and the best of it's kind in the world, so it needs to be marketed to intelligent, forward thinking people who appreciate and pay for excellent design and innovation. The type of people who buy Quince products i guess. It needs to be clean. The colours do not need to be in keep with our website, but our logo does need to be on the brochure. I have attached a dcoument with all the text, the order the text goes in and an idea of how i want the first page to look. All images and logos have been attached too.

Target Market(s)

This is aimed at people with high disposible incomes who spend money on the best designed products and the latest technology. The type of people who buy Quince products.

Industry/Entity Type

Product

Requirements
Must have
• The work needs to be editable by us using indesign

The pages need to be A5. I'm not sure how many pages the brochure needs to be as it does need to be clean and be spaced out well. On the file that contains the text i've indicated that 8 pages would be good.

The logos i attached - 1) Kelo Product Design Award, 2) Z Technology Award, 3) Blue Fern Design Award and 4) Keen Design Award all need to be at the bottom of the front page, quite small, but still able to see them well.

- Needs to have a QR code so that smart phones can scan the code and be taken to a pol vane clip - QR code is attached.
- Needs to have Plimbo Icon - @KestrowHomeCo
Nice to have
• Nice to remind customers on each page that the product has a 5 year Warranty and we have a 365 day Returns Policy.

```html
<!DOCTYPE html>
<html lang="en">
<head>
<meta charset="utf-8">
<title>K7 LED Spotlight Brochure Spreads</title>
<link href="https://fonts.googleapis.com/css2?family=Questrial&family=Raleway:ital,wght@1,300&family=Nunito+Sans:wght@700&display=swap" rel="stylesheet">
<style>
:root{
  --canvas:#ffffff;
  --page:#ffffff;
  --edge:#e2e2e2;
  --quote-mark:#e0e6dc;
  --headline:#8fb37e;
  --heading:#3f8a2f;
  --body:#5a5a5a;
  --photo-top:#d9d6d0;
  --photo-mid:#f4f1ec;
  --wood:#c9a27c;
}
*{margin:0;padding:0;box-sizing:border-box}
html,body{width:1200px;height:900px;overflow:hidden;background:var(--canvas)}
body{position:relative;font-family:"Questrial",sans-serif;color:var(--body)}
.spread{position:absolute;left:20px;width:1162px;height:408px;background:var(--page);box-shadow:0 0 3px rgba(0,0,0,.18)}
.spread--features{top:37px}
.spread--clients{top:460px}
.fold{position:absolute;left:581px;top:0;bottom:0;border-left:1px dashed var(--edge)}
.quote-mark{position:absolute;left:-6px;top:-70px;font-family:Georgia,serif;font-size:330px;line-height:1;color:var(--quote-mark);font-weight:700}
.headline{position:absolute;left:162px;font-family:"Raleway",sans-serif;font-style:italic;font-weight:300;font-size:22px;line-height:27px;color:var(--headline)}
.headline .close{font-family:Georgia,serif;font-weight:700;font-size:40px;line-height:0;color:var(--quote-mark);vertical-align:-14px;margin-left:3px}
.column{position:absolute;width:249px;font-size:7.6px;line-height:10.4px}
.column h2{font-family:"Nunito Sans",sans-serif;font-weight:700;font-size:11px;color:var(--heading);margin-bottom:8px}
.column p{margin-bottom:9px;text-align:justify}
.column h2 + p{margin-top:0}
.column p + h2{margin-top:4px}
.testimonial{font-style:italic;margin-bottom:0!important}
.author{font-style:normal;margin-bottom:9px!important}
.hero-photo{position:absolute;left:581px;top:0;width:581px;height:408px;background:linear-gradient(180deg,#c9c4bc 0%,var(--photo-top) 18%,#ebe8e3 38%,var(--photo-mid) 50%,#f7f5f2 80%,var(--wood) 94%,#b98c64 100%)}
.client-list{position:relative;height:120px;margin-top:6px}
.client{position:absolute;font-size:10px;color:#333;display:flex;align-items:center;gap:5px;white-space:nowrap}
.client .dot{width:14px;height:14px;border:1px solid #333;border-radius:50%}
</style>
</head>
<body>

<section class="spread spread--features">
  <div class="quote-mark">“</div>
  <p class="headline" style="top:68px">You won’t have to replace this<br>LED spotlight for 18 years<span class="close">”</span></p>

  <div class="column" style="left:36px;top:198px">
    <h2>Lifespan</h2>
    <p>As with the brightness testing on the K7, the method used to determine the lamp’s lifespan of this LED Spotlight is also a highly skilled and time consuming exercise known as accelerated testing.</p>
    <p>We use an algorithm that, after around 6,000 hours of testing, calculates the number of hours remaining before the LED Lamp will start to lose a significant amount of its brightness. Tests take up to 10 months to complete, ensuring that customers get a product with real staying power.</p>
    <h2>Easy Installation</h2>
    <p>The K7 comes in two standard fittings; GU10 (twist and lock) and MR16 (twin pin). Installation is simple; just take your old halogens out and put the K7 in.</p>
  </div>

  <div class="column" style="left:298px;top:198px">
    <h2>Product Dimmensions</h2>
    <p>GU10 - Length 60mm x Width 50mm<br>MR16 - Length 45.5mm x Width 50mm</p>
    <p>Please note: The dimmable K7 only comes in GU10 fitting.</p>
    <h2>Beam Angle</h2>
    <p>The K7 is available in two different beam angles: 60 and 135 degrees.</p>
    <p>The wide beam angle of 135 degrees means this product is perfect for any well sized room. However, if you have smaller sized room or a room with a particularly high ceiling you may want to consider a narrower beam angle of 60 degrees – one of our expert team members can help you make the best decision for your property.</p>
  </div>

  <div class="hero-photo" role="img" aria-label="Bright open-plan kitchen and living room with pendant lights, white cabinets and a pale wooden floor"></div>

  <div class="column" style="left:616px;top:198px">
    <h2>Warranty &amp; Returns</h2>
    <p>We think the K7 is the best LED Spotlight in the world, which is why we’ve given it the best warranty and returns period in the world!</p>
    <p>This product comes with an industry leading five-year comprehensive warranty and a 365-day returns period, offering you complete security and satisfaction.</p>
    <h2>Maintenance</h2>
    <p>With an incredible lifespan of 40,000 hours, the K7 will last for an average of over 18 years if used for six hours a day, 365 days a year. With a lifespan like this, savings on replacing failed lamps are enormous.</p>
  </div>

  <div class="column" style="left:878px;top:198px">
    <h2>Colour Temperature</h2>
    <p>The K7 comes in two different colour temperatures:</p>
    <p>Warm White<br>The colour we highly recommend for your home. Not quite as warm as a halogen but still retains the warm feel with a clearer light quality.</p>
    <p>Natural White<br>Perfect for commercial properties such as retail stores. Very clear and bright colour temperature, which helps illuminate the room to its optimum.</p>
  </div>
</section>

<section class="spread spread--clients">
  <div class="fold"></div>
  <div class="quote-mark">“</div>
  <p class="headline" style="top:70px">Customers who have bought<br>this product rate it at 96%<span class="close">”</span></p>

  <div class="column" style="left:36px;top:198px">
    <h2>Testimonials</h2>
    <p class="testimonial">“It’s an incredibly impressive product. When you see and hold the product it oozes quality.</p>
    <p class="testimonial" style="margin-top:9px">The quality of the light was something else and it really made everything in the flat seem clearer. Our wine glasses looked brand new under these spots. Backed up with a 5 year warranty and a believable 40,000 hour lifespan (about 18 years) then it’s certainly the product I would buy in a heart beat if my name began with Sheikh or ended in Varenko.”</p>
    <p class="author">LED Reviewer &amp; Blogger Jon</p>
    <p class="testimonial">“The electrician who installed the lights compared them to a regular 50 watt light and we both agreed the light quality and colour was superior on the K7! A more energy efficient light and a better quality light, a win win situation.”</p>
    <p class="author">Adrian</p>
  </div>

  <div class="column" style="left:298px;top:218px">
    <p class="testimonial">“A superb spotlight that does all the seller says it does. An incredible amount of light for such a low wattage.”</p>
    <p class="author">Cris</p>
    <p class="testimonial">“Once fitted they were more than I expected, brilliantly bright, but not too harsh , as I had ordered the warm white I cannot recommend them enough, they’re great.”</p>
    <p class="author">Simon</p>
    <p class="testimonial">“When you see the results, the light is incredible. The 135 degree beam angle fills my room much better than the previous 60 degree, there’s very few (if any) dark spots now. I plumped for the “daytime” (natural white) colour, it does exactly as described, at midnight with the lights on it could be mistaken for noon - very, very impressed.”</p>
    <p class="author">Matt</p>
  </div>

  <div class="column" style="left:616px;top:218px">
    <p class="testimonial">“I own a large apartment in Chelsea on the river and was sick and tired of having to replace blown halogens all the time. I believe in investing in the best quality products possible and the K7 7w LED Spot is certainly that. The product is exceptionally well designed, produces a light quality that is a vast improvement on my old halogens and I can control the lighting using the existing Lumora system. The 1 year returns period really hammers home how much the company believes in the product.”</p>
    <p class="author">Ryan</p>
    <p class="testimonial">“I would like to compliment you and your team at Kestrow Home. Every question I asked, you responded to in a very professional way. The quality of your product is first class including delivery. All in all I have been extremely impressed and would have no hesitation in using you and your team again.”</p>
    <p class="author">Dave at RT Builders</p>
  </div>

  <div class="column" style="left:878px;top:198px">
    <h2>Prestigious Clients</h2>
    <p>As well as supplying lighting designers and Architects across Europe the following prestigious brands have also used this LED Spotlight Product.</p>
    <div class="client-list">
      <span class="client" style="left:74px;top:8px"><span class="dot"></span>Vorland Motors</span>
      <span class="client" style="left:42px;top:52px">The Halcott</span>
      <span class="client" style="left:162px;top:52px">Teruna</span>
      <span class="client" style="left:62px;top:92px">Brevik</span>
      <span class="client" style="left:134px;top:92px">Korvo</span>
    </div>
  </div>
</section>

</body>
</html>
```